Modern card design needed for building development company

We are looking for a sharp modern new look for our business cards.
We are a New Zealand based company called TKV Ventures NZ LTD that specialises in subdividing large sections, housing and commercial buildings.
We have attached a photo of the current logo and would like to see it improved somehow as it looks a bit dated.
We are open to any colours.

Target Market(s)

Investors, Property buyers

Industry/Entity Type

Investment

Contact Information for Business Card

TKV VENTURES NZ LTD
www.tkvventuresnz.co.nz

Howard Pennick
Phone +64 21 843 192
Email hdpennick@fernmail.co.nz

Font styles to use
Serif
Sans Serif

Colors
0792cd
33a6d7
85cae6
6b449b
886aae
f04a50
ec1f27
f37122
f68d4d

Requirements
Must have
• Please try and make the logo more modern or if you have a similar one we would like to see it.

```html
<!DOCTYPE html>
<html lang="en">
<head>
<meta charset="utf-8">
<title>TKV Ventures NZ LTD – Business Card</title>
<link rel="stylesheet" href="https://fonts.googleapis.com/css2?family=Tinos:ital,wght@0,400;1,400&display=swap">
<style>
  :root {
    --backdrop: #5f6573;
    --card: #e8e7e5;
    --maroon: #9b1b30;
    --ink: #1c1c1c;
    --red: #ec1f27;
    --coral: #f0585c;
    --orange: #f37f2e;
    --purple: #6b52a1;
    --sky: #4aa3db;
  }
  * { box-sizing: border-box; margin: 0; padding: 0; }
  html, body { width: 1200px; height: 1200px; overflow: hidden; }
  body {
    background: var(--backdrop);
    position: relative;
    font-family: "Tinos", "Times New Roman", serif;
  }
  .card {
    position: absolute;
    width: 857px;
    height: 488px;
    background: var(--card);
    overflow: hidden;
  }
  .card--front { left: 23px; top: 82px; }
  .card--back { left: 269px; top: 640px; width: 854px; }

  .card__colour-field {
    position: absolute;
    left: 0;
    top: 0;
    width: 335px;
    height: 100%;
    background: linear-gradient(120deg, var(--red) 0%, var(--coral) 35%, var(--orange) 60%, var(--purple) 80%, var(--sky) 100%);
  }

  .company-name {
    position: absolute;
    right: 14px;
    top: 40px;
    font-style: italic;
    font-weight: 400;
    font-size: 54px;
    line-height: 1;
    color: var(--maroon);
    white-space: nowrap;
  }
  .tagline {
    position: absolute;
    right: 78px;
    top: 99px;
    font-style: italic;
    font-size: 13px;
    color: var(--ink);
    white-space: nowrap;
  }
  .brand-mark {
    position: absolute;
    left: 414px;
    top: 146px;
    width: 430px;
    height: 342px;
    display: flex;
    align-items: center;
    justify-content: center;
    gap: 18px;
  }
  .brand-mark__square {
    width: 46px;
    height: 46px;
    background: var(--maroon);
  }
  .brand-mark__name {
    font-style: italic;
    font-size: 50px;
    color: var(--maroon);
    white-space: nowrap;
  }

  .person-name {
    position: absolute;
    font-style: italic;
    font-weight: 400;
    font-size: 84px;
    line-height: 1;
    color: var(--ink);
    letter-spacing: 2px;
    white-space: nowrap;
  }
  .person-name--first { left: 359px; top: 62px; }
  .person-name--last { right: 31px; top: 160px; }

  .contact-list { list-style: none; }
  .contact-item {
    position: absolute;
    right: 25px;
    height: 44px;
    display: flex;
    align-items: center;
    gap: 22px;
    font-style: italic;
    font-size: 26px;
    letter-spacing: 1.5px;
    color: var(--ink);
    white-space: nowrap;
  }
  .contact-item--phone { top: 270px; }
  .contact-item--email { top: 318px; }
  .contact-item--web { top: 370px; }
  .contact-icon { width: 44px; height: 44px; flex: none; }
  .contact-icon circle, .contact-icon .line { fill: none; stroke: var(--ink); stroke-width: 2; }
</style>
</head>
<body>

<section class="card card--front">
  <div class="card__colour-field" role="img" aria-label="Decorative multicoloured band artwork"></div>
  <h1 class="company-name">TKV Ventures NZ LTD</h1>
  <p class="tagline">specialises in subdividing large sections, housing and commercial buildings</p>
  <div class="brand-mark">
    <span class="brand-mark__square"></span>
    <span class="brand-mark__name">TKV Ventures</span>
  </div>
</section>

<section class="card card--back">
  <div class="card__colour-field" role="img" aria-label="Decorative multicoloured band artwork"></div>
  <h2 class="person-name person-name--first">Howard</h2>
  <h2 class="person-name person-name--last">Pennick</h2>
  <ul class="contact-list">
    <li class="contact-item contact-item--phone">
      <span>+64 21 843 192</span>
      <svg class="contact-icon" viewBox="0 0 44 44" aria-hidden="true">
        <circle cx="22" cy="22" r="20"/>
        <path d="M15 12c2-1 3 0 4 3s0 3-1 4c1 3 4 6 7 7 1-1 2-2 4-1s4 2 3 4c-1 3-4 3-7 2-5-2-10-7-12-12-1-3 0-6 2-7z" fill="#1c1c1c"/>
      </svg>
    </li>
    <li class="contact-item contact-item--email">
      <span>hdpennick@fernmail.co.nz</span>
      <svg class="contact-icon" viewBox="0 0 44 44" aria-hidden="true">
        <circle cx="22" cy="22" r="20"/>
        <rect class="line" x="11" y="14" width="22" height="16"/>
        <polyline class="line" points="11,14 22,24 33,14"/>
        <polyline class="line" points="11,30 19,21"/>
        <polyline class="line" points="33,30 25,21"/>
      </svg>
    </li>
    <li class="contact-item contact-item--web">
      <span>www.tkvventuresnz.co.nz</span>
      <svg class="contact-icon" viewBox="0 0 44 44" aria-hidden="true">
        <circle cx="22" cy="22" r="20"/>
        <rect class="line" x="12" y="12" width="20" height="14" rx="1"/>
        <rect class="line" x="13" y="29" width="18" height="4" rx="1"/>
        <path d="M24 16l5 4-2.5 .5 1.5 3-1.5.7-1.5-3-1.5 1.6z" fill="#1c1c1c"/>
      </svg>
    </li>
  </ul>
</section>

</body>
</html>
```